Summit Tandem Trial Poster

I need an 11x17 poster using the details attached.

I also attached a poster that I got through PixelHarbor and used for our last contest so you know what I liked. I am not looking for the same thing I am just including it so you know my taste. Clean and effective.

Included is the Vorduna Bootcamps logo as well.

```html
<!DOCTYPE html>
<html lang="en">
<head>
<meta charset="utf-8">
<title>Summit Tandem Trial Poster</title>
<link href="https://fonts.googleapis.com/css2?family=Alfa+Slab+One&family=Arimo:ital,wght@0,400;0,700;1,700&display=swap" rel="stylesheet">
<style>
  :root {
    --ink: #141414;
    --headline-blue: #2f5fb5;
    --band-orange: #c27a2f;
    --band-edge: #6e3f14;
    --panel-blue: #5d8fd3;
    --panel-ink: #15151f;
    --paper: #ffffff;
    --photo-warm: #c9a487;
    --photo-cool: #8d7a8e;
  }
  * { margin: 0; padding: 0; box-sizing: border-box; }
  html, body { width: 776px; height: 1200px; overflow: hidden; background: var(--paper); }
  .poster {
    position: relative;
    width: 776px;
    height: 1200px;
    background: var(--paper);
    font-family: "Arimo", Arial, sans-serif;
    color: var(--ink);
    overflow: hidden;
  }
  .headline {
    position: absolute;
    left: 0; right: 0; top: 22px;
    text-align: center;
    font-family: "Alfa Slab One", Georgia, serif;
    font-size: 40px;
    line-height: 50px;
    font-weight: 400;
  }
  .headline .accent {
    display: block;
    color: var(--headline-blue);
    font-size: 40px;
    margin-top: 4px;
    letter-spacing: 0.5px;
  }
  .band {
    position: absolute;
    left: 0; width: 776px;
    background: var(--band-orange);
    border-top: 2px solid var(--band-edge);
    border-bottom: 2px solid var(--band-edge);
  }
  .band--top { top: 182px; height: 40px; }
  .band--middle { top: 420px; height: 42px; }
  .band--bottom { top: 738px; height: 32px; }
  .team-photo {
    position: absolute;
    left: 0; top: 222px;
    width: 776px; height: 198px;
    background: linear-gradient(90deg, var(--photo-warm), var(--photo-cool) 35%, var(--photo-warm) 60%, var(--photo-cool));
  }
  .event-title {
    position: absolute;
    left: 0; right: 0; top: 468px;
    text-align: center;
    font-family: "Alfa Slab One", Georgia, serif;
    font-size: 46px;
    line-height: 56px;
    letter-spacing: 0.5px;
  }
  .details {
    position: absolute;
    left: 24px; top: 534px;
    width: 730px;
    list-style: none;
    font-size: 18px;
    line-height: 25px;
  }
  .details li {
    position: relative;
    padding-left: 30px;
    margin-bottom: 13px;
  }
  .details li::before {
    content: "";
    position: absolute;
    left: 0; top: 6px;
    width: 13px; height: 13px;
    background: var(--ink);
  }
  .details strong { font-weight: 700; }
  .info-panel {
    position: absolute;
    left: 0; top: 770px;
    width: 776px; height: 430px;
    background: var(--panel-blue);
    color: var(--panel-ink);
    text-align: center;
  }
  .contest-info {
    position: absolute;
    left: 0; right: 0; top: 18px;
    font-style: italic;
    font-weight: 700;
    font-size: 24px;
    line-height: 30px;
  }
  .phone {
    position: absolute;
    left: 0; right: 0; top: 96px;
    font-family: "Arimo", Arial, sans-serif;
    font-weight: 700;
    font-size: 64px;
    line-height: 70px;
    letter-spacing: 2px;
  }
  .call-to-action {
    position: absolute;
    left: 0; right: 0; top: 196px;
    font-family: "Alfa Slab One", Georgia, serif;
    font-size: 27px;
    line-height: 34px;
  }
  .website {
    position: absolute;
    left: 0; right: 0; top: 238px;
    font-family: "Alfa Slab One", Georgia, serif;
    font-size: 25px;
    line-height: 32px;
    letter-spacing: 0.5px;
  }
  .brand-name {
    position: absolute;
    left: 0; right: 0; top: 326px;
    font-family: "Alfa Slab One", Georgia, serif;
    font-size: 38px;
    line-height: 46px;
    color: var(--panel-ink);
  }
</style>
</head>
<body>
<main class="poster">
  <h1 class="headline">
    Looking For A Good Reason<br>
    To Get in the
    <span class="accent">BEST SHAPE OF YOUR LIFE?</span>
  </h1>

  <div class="band band--top"></div>
  <div class="team-photo" role="img" aria-label="Photo of a line-up of smiling men and women of different ages in workout clothes, holding water bottles, dumbbells and yoga mats"></div>
  <div class="band band--middle"></div>

  <h2 class="event-title">SUMMIT TANDEM TRIAL</h2>

  <ul class="details">
    <li>21 Day Fitness Challenge offers <strong>World Class Training and Testing</strong> to ensure that you are prepared to take on anything life throws at you.</li>
    <li>During the <strong>SUMMIT TANDEM TRIAL</strong> you will be tested on your initial fitness skills, trained in an intesnse training program for 21 days and re-tested to see which team made the most improvement.</li>
    <li><strong>Male, Female and Co-Ed Divisions</strong>.</li>
  </ul>

  <div class="band band--bottom"></div>

  <section class="info-panel">
    <p class="contest-info">
      Contest Dates: January 26th - February 15th<br>
      Over $700 in cash prizes are up for grabs<br>
      for the best Team Scores and Best Improvement!
    </p>
    <p class="phone">555.014.7820</p>
    <p class="call-to-action">Call To Researve Your Spot Today!</p>
    <p class="website">www.VordunaFit.com</p>
    <p class="brand-name">Vorduna Bootcamps</p>
  </section>
</main>
</body>
</html>
```